Tarvick homes and renovations business card design.

Would like some new card designs utilizing my new logo that look professional. I am open to different colors on the logo or utilize the same ones we have. I like the original concept but would like to see some fresh ideas and build on what we have already done.

Target Market(s)

Custom home building industry, Real estate sales, Renovation projects.

Industry/Entity Type

Home Builder

Contact Information for Business Card

Tarvick Homes and Renovations
2871 92nd Avenue
Frank, Alberta
R3J2W5
Home : 403- 718-4305 Cell: 403- 294-1537

My info is : Dax Tarvick, President and CEO
email: tarvickhomes@quillpost.net
Website: tarvickhomes.net

Requirements
Must have
• Must Use my new logo design. I am open to different colors on the logo or utilize the same ones in the existing design. I can upload the original logo design if needed.

```html
<!DOCTYPE html>
<html lang="en">
<head>
<meta charset="utf-8">
<title>Tarvick Homes and Renovations – Business Card</title>
<link href="https://fonts.googleapis.com/css2?family=Cormorant+Garamond:wght@600&display=swap" rel="stylesheet">
<style>
  :root {
    --backdrop: #e6e7e9;
    --card-black: #050505;
    --band-dark: #2a1f05;
    --band-light: #4a3a12;
    --gold: #d9a50c;
    --gold-bright: #f2c200;
    --card-width: 880px;
    --card-height: 503px;
  }
  * { box-sizing: border-box; margin: 0; padding: 0; }
  html, body {
    width: 1200px;
    height: 1200px;
    overflow: hidden;
    background: var(--backdrop);
  }
  body {
    display: flex;
    flex-direction: column;
    align-items: center;
    justify-content: center;
    gap: 60px;
    font-family: "Cormorant Garamond", Georgia, serif;
    font-weight: 600;
  }
  .card {
    position: relative;
    width: var(--card-width);
    height: var(--card-height);
    background: var(--card-black);
    overflow: hidden;
    box-shadow: 0 14px 30px rgba(0,0,0,0.18);
  }
  .top-band {
    position: absolute;
    inset: 0;
    width: 100%;
    height: 100%;
  }
  .brand-name {
    color: var(--gold);
    font-size: 38px;
    line-height: 1.05;
    letter-spacing: 0.5px;
  }
  .brand-mark {
    display: inline-block;
    width: 14px;
    height: 14px;
    background: var(--gold);
    margin-right: 12px;
    vertical-align: middle;
  }
  .front .brand {
    position: absolute;
    left: 70px;
    top: 210px;
    width: 330px;
  }
  .front .divider {
    position: absolute;
    left: 440px;
    top: 215px;
    width: 2px;
    height: 170px;
    background: var(--gold-bright);
  }
  .contact-list {
    position: absolute;
    left: 470px;
    top: 215px;
    list-style: none;
    color: var(--gold);
    font-size: 27px;
    line-height: 1.3;
  }
  .contact-list li { display: flex; align-items: flex-start; gap: 10px; }
  .contact-list .address { margin-top: 14px; }
  .contact-list svg { width: 18px; height: 18px; margin-top: 8px; flex: none; fill: var(--gold-bright); }
  .back {
    display: flex;
    align-items: center;
    justify-content: center;
  }
  .back .brand-name { font-size: 46px; text-align: center; }
</style>
</head>
<body>

  <section class="card front" aria-label="Card front">
    <svg class="top-band" viewBox="0 0 880 503" preserveAspectRatio="none" aria-hidden="true">
      <defs>
        <linearGradient id="bandShade" x1="0" y1="0" x2="1" y2="1">
          <stop offset="0" stop-color="var(--band-dark)"/>
          <stop offset="1" stop-color="var(--band-light)"/>
        </linearGradient>
      </defs>
      <polygon points="0,0 880,0 880,230 560,95 140,115 0,120" fill="url(#bandShade)"/>
    </svg>

    <div class="brand">
      <p class="brand-name"><span class="brand-mark"></span>Tarvick Homes and Renovations</p>
    </div>

    <div class="divider"></div>

    <ul class="contact-list">
      <li>
        <svg viewBox="0 0 16 16"><rect x="4" y="1" width="8" height="14" rx="1.5"/><rect x="5.5" y="3" width="5" height="7" fill="var(--card-black)"/></svg>
        <span>403- 294-1537</span>
      </li>
      <li>
        <svg viewBox="0 0 16 16"><path d="M1 6c0-2 3-3 7-3s7 1 7 3v1h-4V5.5H5V7H1z"/><rect x="3" y="8" width="10" height="6" rx="1"/></svg>
        <span>403- 718-4305</span>
      </li>
      <li class="address">
        <svg viewBox="0 0 16 16"><path d="M8 1 1 8h2v7h4v-4h2v4h4V8h2z"/></svg>
        <span>2871 92nd Avenue<br>Frank, Alberta, R3J2W5</span>
      </li>
    </ul>
  </section>

  <section class="card back" aria-label="Card back">
    <p class="brand-name"><span class="brand-mark"></span>Tarvick Homes and Renovations</p>
  </section>

</body>
</html>
```